Folded A4 flyer for design&construction company

Folded A4 flyer needed. Keywords: elegant, stylish
our website www.corvimo.ae

Industry/Entity Type

Construction

```html
<!DOCTYPE html>
<html lang="en">
<head>
<meta charset="utf-8">
<title>Corvimo – Folded Flyer</title>
<link href="https://fonts.googleapis.com/css2?family=Josefin+Sans:wght@400&family=Raleway:wght@300;400;500;800&family=Great+Vibes&display=swap" rel="stylesheet">
<style>
  :root{
    --bg:#3b3b3b;
    --paper:#ffffff;
    --ink:#111111;
    --text:#555555;
    --gold-dark:#a8872a;
    --gold:#c9a83a;
    --gold-light:#ecd366;
    --charcoal:#4a4a4a;
    --bracket:#cfcfcf;
  }
  *{box-sizing:border-box;margin:0;padding:0}
  html,body{width:918px;height:1200px;overflow:hidden}
  body{background:var(--bg);font-family:"Raleway",sans-serif;color:var(--text);position:relative}
  .spread{position:absolute;left:79px;width:760px;height:538px;background:var(--paper);box-shadow:0 6px 18px rgba(0,0,0,.5);overflow:hidden}
  .spread--outer{top:56px}
  .spread--inner{top:606px}
  .spread svg.shapes{position:absolute;left:0;top:0;width:760px;height:538px}
  .fold{position:absolute;left:380px;top:0;width:1px;height:538px;background:#2a2a2a;opacity:.55}
  .abs{position:absolute}

  .intro{left:33px;top:40px;width:326px;font-size:9.4px;line-height:13.6px;text-align:justify;font-weight:300;color:#4a4a4a}

  .quote-box{left:57px;top:306px;width:270px;height:112px;background:var(--charcoal);border-radius:0 0 16px 16px;color:#fff;text-align:center;padding-top:34px;box-shadow:0 4px 8px rgba(0,0,0,.3)}
  .quote-box__lead{font-size:13px;font-weight:300;letter-spacing:.2px}
  .quote-box__lead strong{font-weight:800}
  .quote-box__phone{font-size:25px;font-weight:500;line-height:32px}
  .quote-box__mail{font-size:11.5px;font-weight:500}

  .contact{left:32px;font-size:9.6px;color:#fff;font-weight:300;line-height:13px;display:flex;gap:8px;align-items:flex-start}
  .contact strong{font-weight:500}
  .contact svg{width:14px;height:14px;flex:none}
  .contact--web{top:462px}
  .contact--addr{top:480px}

  .brand{position:absolute;text-align:center;transform:translateX(-50%)}
  .brand__name{font-family:"Josefin Sans",sans-serif;font-weight:400;color:var(--ink);line-height:1;letter-spacing:1px}
  .brand__tag{color:var(--gold-dark);font-size:13px;margin-top:6px;letter-spacing:.5px}
  .brand__sub{display:flex;align-items:center;gap:5px;justify-content:center;color:var(--gold-dark);font-size:12px;font-weight:500;letter-spacing:.5px;margin-top:3px}
  .brand__sub::before,.brand__sub::after{content:"";flex:1;height:1.5px;background:var(--gold-dark)}
  .brand--hero{left:565px;top:112px;width:220px}
  .brand--hero .brand__name{font-size:46px}
  .brand--small{width:140px}
  .brand--small .brand__name{font-size:30px}

  .motto{left:380px;width:380px;top:382px;text-align:center;color:var(--ink);font-family:"Great Vibes",cursive;font-size:36px;line-height:38px}
  .motto__by{font-family:"Raleway",sans-serif;font-size:13px;color:#fff;font-weight:300;margin-top:4px;line-height:16px}

  .services{position:absolute;list-style:none;padding:8px 12px 6px 18px;font-size:9.6px;line-height:16.8px;color:#333;white-space:nowrap}
  .services::before,.services::after{content:"";position:absolute;top:0;bottom:0;width:10px;border:4px solid var(--bracket)}
  .services::before{left:0;border-right:none}
  .services::after{right:0;border-left:none}
  .services li{position:relative;padding-left:12px}
  .services li::before{content:"·";position:absolute;left:0;font-weight:800}
  .services li.two-line{line-height:13.6px;padding-top:2px}
  .services--design{left:192px;top:34px;width:172px}
  .services--landscape{left:192px;top:219px;width:172px;padding-left:25px}
  .services--fitout{left:565px;top:86px;width:168px}
  .services--maint{left:565px;top:258px;width:168px;padding-left:26px}
</style>
</head>
<body>

<section class="spread spread--outer">
  <svg class="shapes" viewBox="0 0 760 538">
    <defs>
      <radialGradient id="goldGlow" cx="0.6" cy="0.75" r="0.8">
        <stop offset="0" stop-color="#efd66a"/>
        <stop offset="0.55" stop-color="#cfae3f"/>
        <stop offset="1" stop-color="#a8872a"/>
      </radialGradient>
      <linearGradient id="lounge" x1="0" y1="0" x2="1" y2="1">
        <stop offset="0" stop-color="#4a3526"/>
        <stop offset="0.5" stop-color="#8a6446"/>
        <stop offset="1" stop-color="#c79a6e"/>
      </linearGradient>
      <radialGradient id="warmRoom" cx="0.5" cy="0.5" r="0.6">
        <stop offset="0" stop-color="#f0d9a8"/>
        <stop offset="1" stop-color="#a8763a"/>
      </radialGradient>
    </defs>
    <path d="M0,380 C110,330 250,318 380,322 L380,538 L0,538 Z" fill="url(#goldGlow)"/>
    <g role="img" aria-label="Photo of a modern lounge with two cream armchairs, wood floor and fireplace">
      <path d="M0,178 C130,146 250,160 380,240 L380,306 C250,288 110,318 0,350 Z" fill="url(#lounge)"/>
    </g>
    <path d="M0,168 C130,136 250,150 380,232 L380,244 C250,164 130,150 0,182 Z" fill="var(--ink)"/>
    <path d="M380,318 C520,330 660,300 760,240 L760,538 L380,538 Z" fill="url(#goldGlow)"/>
    <path d="M640,300 C690,290 730,262 760,230 L760,256 C728,282 690,300 640,300 Z" fill="var(--ink)"/>
    <g role="img" aria-label="Round photo of a bright yellow reception interior">
      <circle cx="457" cy="280" r="52" fill="#fff"/>
      <circle cx="457" cy="280" r="47" fill="url(#warmRoom)"/>
    </g>
    <g role="img" aria-label="Round photo of a classic villa hallway">
      <circle cx="565" cy="280" r="52" fill="#fff"/>
      <circle cx="565" cy="280" r="47" fill="url(#warmRoom)"/>
    </g>
    <g role="img" aria-label="Round photo of a luxurious living room with chandelier">
      <circle cx="673" cy="280" r="52" fill="#fff"/>
      <circle cx="673" cy="280" r="47" fill="url(#warmRoom)"/>
    </g>
  </svg>
  <div class="fold"></div>

  <p class="abs intro">We believe in quality beginnings and flawless finishes. We are a team of creative designers and constructors with years of experience and expertise in providing complete interior design and construction services. Our unique designing prowess is complemented by our unflinching commitment to quality construction. Our team specializes in classic and contemporary high quality construction in Dubai for commercial and residential projects.</p>

  <div class="abs quote-box">
    <p class="quote-box__lead">GET A <strong>FREE QUOTE</strong> TODAY!</p>
    <p class="quote-box__phone">800 – CORVIMO</p>
    <p class="quote-box__mail">OR CONTACT@CORVIMO.AE</p>
  </div>

  <p class="abs contact contact--web">
    <svg viewBox="0 0 14 14"><circle cx="7" cy="7" r="6" fill="none" stroke="#fff" stroke-width="1.2"/><path d="M1 7h12M7 1c-3 3.5-3 8.5 0 12M7 1c3 3.5 3 8.5 0 12" fill="none" stroke="#fff" stroke-width=".9"/></svg>
    <span>www.<strong>corvimo</strong>.ae</span>
  </p>
  <p class="abs contact contact--addr">
    <svg viewBox="0 0 14 14"><circle cx="7" cy="7" r="6" fill="none" stroke="#fff" stroke-width="1.2"/><path d="M3.5 7.2 7 4l3.5 3.2V10h-7z" fill="#fff"/></svg>
    <span>Corvimo LLC, Harbor Point Tower,<br>Office 1304, Business Bay, Dubai</span>
  </p>

  <div class="brand brand--hero">
    <p class="brand__name">CORVIMO</p>
    <p class="brand__tag">design &amp; construction</p>
  </div>

  <div class="abs motto">
    <p>Quality is not an act,<br>it is a habit</p>
    <p class="motto__by">– Elias Varro</p>
  </div>
</section>

<section class="spread spread--inner">
  <svg class="shapes" viewBox="0 0 760 538">
    <defs>
      <radialGradient id="goldGlow2" cx="0.6" cy="0.5" r="0.8">
        <stop offset="0" stop-color="#efd66a"/>
        <stop offset="0.6" stop-color="#cfae3f"/>
        <stop offset="1" stop-color="#a8872a"/>
      </radialGradient>
      <linearGradient id="dining" x1="0" y1="0" x2="1" y2="0">
        <stop offset="0" stop-color="#5a5560"/>
        <stop offset="0.5" stop-color="#d8d6da"/>
        <stop offset="1" stop-color="#6b5a44"/>
      </linearGradient>
      <linearGradient id="ceiling" x1="0" y1="0" x2="1" y2="0">
        <stop offset="0" stop-color="#8a8fa8"/>
        <stop offset="1" stop-color="#2e2e36"/>
      </linearGradient>
      <radialGradient id="roomWarm" cx="0.5" cy="0.5" r="0.6">
        <stop offset="0" stop-color="#e8d2a4"/>
        <stop offset="1" stop-color="#5a4430"/>
      </radialGradient>
    </defs>
    <path d="M0,520 C120,500 250,470 380,478 L380,538 L0,538 Z" fill="url(#goldGlow2)"/>
    <g role="img" aria-label="Photo of a modern dining room with purple velvet chairs and glass table">
      <path d="M0,360 C110,338 250,340 380,400 L380,470 C250,440 110,470 0,520 Z" fill="url(#dining)"/>
    </g>
    <path d="M0,348 C110,326 250,328 380,390 L380,402 C250,342 110,340 0,362 Z" fill="var(--ink)"/>
    <g role="img" aria-label="Photo of a curved ceiling with dark slats and spotlights">
      <path d="M420,0 L760,0 L760,66 C640,74 530,40 420,0 Z" fill="url(#ceiling)"/>
    </g>
    <path d="M420,0 C530,40 640,74 760,66 L760,82 C640,88 520,50 420,0 Z" fill="var(--ink)"/>
    <path d="M380,470 C520,480 660,460 760,408 L760,538 L380,538 Z" fill="url(#goldGlow2)"/>
    <path d="M690,440 C720,430 742,416 760,400 L760,420 C740,434 718,442 690,440 Z" fill="var(--ink)"/>
    <g role="img" aria-label="Round photo of a warm lit wellness lounge">
      <circle cx="445" cy="466" r="52" fill="#fff"/>
      <circle cx="445" cy="466" r="47" fill="url(#roomWarm)"/>
    </g>
    <g role="img" aria-label="Round photo of a bathroom with freestanding tub and chandelier">
      <circle cx="553" cy="466" r="52" fill="#fff"/>
      <circle cx="553" cy="466" r="47" fill="url(#roomWarm)"/>
    </g>
    <g role="img" aria-label="Round photo of a bedroom with patterned feature wall">
      <circle cx="661" cy="466" r="52" fill="#fff"/>
      <circle cx="661" cy="466" r="47" fill="url(#roomWarm)"/>
    </g>
  </svg>
  <div class="fold"></div>

  <div class="brand brand--small" style="left:101px;top:92px">
    <p class="brand__name">CORVIMO</p>
    <p class="brand__sub">DESIGN</p>
  </div>
  <ul class="services services--design">
    <li>Villas Interior Design</li>
    <li>Villas Exterior Design</li>
    <li>Landscape Design</li>
    <li>Retail Interior Design</li>
    <li>Office Interior Design</li>
    <li>Hospitality Interior Design</li>
    <li>Hotel Interior Design</li>
    <li>Hotel Exterior Design</li>
    <li>Restaurant Interior Design</li>
  </ul>

  <div class="brand brand--small" style="left:101px;top:272px">
    <p class="brand__name">CORVIMO</p>
    <p class="brand__sub">LANDSCAPING</p>
  </div>
  <ul class="services services--landscape">
    <li>Soft Landscaping</li>
    <li>Irrigation Solutions</li>
    <li>Hard land Scaping</li>
    <li>External Lighting</li>
    <li class="two-line">Swimming Pool &amp;<br>Water Features</li>
  </ul>

  <div class="brand brand--small" style="left:470px;top:140px">
    <p class="brand__name">CORVIMO</p>
    <p class="brand__sub">FITOUT</p>
  </div>
  <ul class="services services--fitout">
    <li>Development Approvals</li>
    <li>Flooring Solutions</li>
    <li>Partition</li>
    <li>Sealing Solutions</li>
    <li>MEP Works</li>
    <li>Civil Works</li>
    <li>Joinery</li>
    <li class="two-line">Glass and Aluminium<br>Works (subcontractor)</li>
  </ul>

  <div class="brand brand--small" style="left:470px;top:312px">
    <p class="brand__name">CORVIMO</p>
    <p class="brand__sub">MAINTAINCE</p>
  </div>
  <ul class="services services--maint">
    <li>AC Repair</li>
    <li>Plumber Services</li>
    <li>Electric Repair</li>
    <li>Carpentry Work</li>
    <li>Gypsum Ceiling</li>
    <li>Painting Services</li>
    <li>Cleaning Services</li>
    <li>Emergency Services</li>
  </ul>
</section>

</body>
</html>
```